Brackenfold Latches Business Cards

Need high quality business card designed around my company logo. Ideally the cards need to be a glossy black as the logo goes well with a black background.

The company is a Locksmithing business.

Domestic clients are Residential Home Owners and Landlords. Commercial clients are local businesses, estate agents, landlords, solicitors

Services offered :
Emergency Lock Out
New Lock Fitting & Replacement
High Security Upgrades
UPVC lock repairs
Mobile Key Cutting
Free Security Reviews

Qualificatons & Certifications:
Accredited Guild & Tower KSR Level 3, QTRB
Fully Insured
PVX Checked

Contact & Business Details:

Business Name : Brackenfold Latches
Name: Rob Fenwick
Tel: 01823 574419 Office / 07841592637 Mobile
Email: contact@brackenfoldlatches.com
Website: www.brackenfoldlatches.com

(please note that the website is currently under development and not available to view)

Locksmith

Name: Rob Fenwick

Services:
Emergency Lock Out
High Security Upgrades
UPVC lock repairs
Mobile Key Cutting
Free Security Reviews

• Ideally the cards should be a glossy black as the logo stands out better on a black background.

Logo on front and the word LOCKSMITH should be incorporated into the front design of the card.

Qualifications & Certifications on the back ideally along the top / bottom of the card or split (I.e along the top “ Accredited : Guild & Tower Level 3 , QTRB”
and along the bottom , “Fully Insured & PVX Checked”

Services offered ideally listed on the back of the card, preferably split into two columns. If possible the logo could also be incorporated onto the back of the card between the two services columns (I.e the services listed either side of the logo)
• On the back of the card, have the logo in the middle with the services listed either side of the logo I.e 3 services on left of logo and three to the right.

```html
<!DOCTYPE html>
<html lang="en">
<head>
<meta charset="utf-8">
<title>Brackenfold Latches Business Cards</title>
<link rel="stylesheet" href="https://fonts.googleapis.com/css2?family=Cinzel:wght@600&family=Open+Sans:wght@400&display=swap">
<style>
  :root {
    --backdrop: #e4e4e4;
    --card-black: #151515;
    --gold-dark: #a9780f;
    --gold-mid: #e9c24a;
    --gold-light: #f6dc7a;
    --gold-text: #d9a92c;
    --band-ink: #2b2108;
    --white: #ffffff;
    --badge-navy: #2a2f6b;
    --gold-gradient: linear-gradient(90deg, var(--gold-dark) 0%, var(--gold-mid) 30%, var(--gold-light) 50%, var(--gold-mid) 70%, var(--gold-dark) 100%);
  }
  * { margin: 0; padding: 0; box-sizing: border-box; }
  html, body { width: 1200px; height: 960px; overflow: hidden; }
  body {
    background: var(--backdrop);
    position: relative;
    font-family: "Open Sans", sans-serif;
  }
  .card {
    position: absolute;
    left: 306px;
    width: 590px;
    height: 337px;
    background: var(--card-black);
    overflow: hidden;
  }
  .card--front { top: 118px; }
  .card--back { top: 520px; }

  /* Front */
  .service-band {
    position: absolute;
    left: 0; right: 0;
    top: 105px;
    height: 127px;
    border-top: 3px solid var(--gold-mid);
    border-bottom: 3px solid var(--gold-mid);
    padding: 4px 0;
    background-clip: content-box;
    background-image: var(--gold-gradient);
  }
  .service-list {
    position: absolute;
    top: 116px;
    width: 200px;
    list-style: none;
    text-align: center;
    color: var(--band-ink);
    font-size: 14.5px;
    line-height: 17px;
  }
  .service-list li { margin-bottom: 16px; }
  .service-list--left { left: 0; width: 194px; top: 121px; }
  .service-list--left li:nth-child(2) { margin-bottom: 11px; }
  .service-list--right { left: 393px; top: 124px; }

  .brand-mark {
    position: absolute;
    border-radius: 50%;
    background: var(--card-black);
    border: 4px solid var(--gold-mid);
    display: flex;
    align-items: center;
    justify-content: center;
    text-align: center;
  }
  .brand-mark__name {
    font-family: "Cinzel", serif;
    font-weight: 600;
    color: var(--gold-text);
    line-height: 1.15;
  }
  .card--front .brand-mark { left: 191px; top: 70px; width: 208px; height: 208px; }
  .card--front .brand-mark__name { font-size: 25px; }
  .card--back .brand-mark { left: 47px; top: 34px; width: 176px; height: 176px; }
  .card--back .brand-mark__name { font-size: 21px; }

  /* Back */
  .accreditations {
    position: absolute;
    top: 37px;
    right: 31px;
    display: flex;
    align-items: center;
    gap: 16px;
  }
  .accreditation { display: block; }
  .accreditation--guild { width: 52px; height: 44px; background: var(--white); border-radius: 3px; }
  .accreditation--level { width: 66px; height: 24px; background: var(--badge-navy); }
  .accreditation--body { width: 68px; height: 24px; background: var(--white); border-radius: 3px; }

  .holder-name {
    position: absolute;
    right: 31px;
    top: 146px;
    font-family: "Cinzel", serif;
    font-weight: 600;
    font-size: 23px;
    letter-spacing: 0.5px;
    color: var(--gold-text);
  }
  .holder-rule {
    position: absolute;
    right: 31px;
    top: 192px;
    width: 37px;
    height: 2px;
    background: var(--gold-mid);
  }
  .contact-list {
    position: absolute;
    right: 31px;
    top: 213px;
    list-style: none;
    text-align: right;
    color: var(--white);
    font-size: 14px;
    line-height: 20px;
  }
  .contact-list li { display: flex; justify-content: flex-end; align-items: center; gap: 5px; }
  .contact-icon { width: 13px; height: 13px; fill: var(--gold-mid); flex: none; }
  .credentials {
    position: absolute;
    left: 56px;
    top: 272px;
    color: var(--white);
    font-size: 14px;
  }
  .gold-strip {
    position: absolute;
    left: 0; right: 0; bottom: 0;
    height: 14px;
    background-image: var(--gold-gradient);
  }
</style>
</head>
<body>

<section class="card card--front" aria-label="Card front">
  <div class="service-band"></div>
  <ul class="service-list service-list--left">
    <li>Emergency Lock Out</li>
    <li>New Lock Fitting<br>&amp; Replacement</li>
    <li>Mobile Key Cutting</li>
  </ul>
  <ul class="service-list service-list--right">
    <li>Free Security Reviews</li>
    <li>UPVC Lock Repairs</li>
    <li>High Security Upgrades</li>
  </ul>
  <div class="brand-mark">
    <span class="brand-mark__name">Brackenfold<br>Latches</span>
  </div>
</section>

<section class="card card--back" aria-label="Card back">
  <div class="brand-mark">
    <span class="brand-mark__name">Brackenfold<br>Latches</span>
  </div>

  <div class="accreditations" aria-label="Accreditations">
    <span class="accreditation accreditation--guild"></span>
    <span class="accreditation accreditation--level"></span>
    <span class="accreditation accreditation--body"></span>
  </div>

  <h2 class="holder-name">ROB FENWICK</h2>
  <div class="holder-rule"></div>

  <ul class="contact-list">
    <li>01823 574419
      <svg class="contact-icon" viewBox="0 0 24 24"><path d="M6.6 10.8a15.1 15.1 0 0 0 6.6 6.6l2.2-2.2a1 1 0 0 1 1-.25 11.4 11.4 0 0 0 3.6.57 1 1 0 0 1 1 1V20a1 1 0 0 1-1 1A17 17 0 0 1 3 4a1 1 0 0 1 1-1h3.5a1 1 0 0 1 1 1c0 1.25.2 2.45.57 3.57a1 1 0 0 1-.25 1z"/></svg>
    </li>
    <li>078 4159 2637
      <svg class="contact-icon" viewBox="0 0 24 24"><path d="M7 1h10a2 2 0 0 1 2 2v18a2 2 0 0 1-2 2H7a2 2 0 0 1-2-2V3a2 2 0 0 1 2-2zm0 3v15h10V4zm5 16.2a1 1 0 1 0 0 .1z"/></svg>
    </li>
    <li>contact@brackenfoldlatches.com
      <svg class="contact-icon" viewBox="0 0 24 24"><path d="M2 5h20v14H2zm2 2v.5l8 5.5 8-5.5V7zm0 2.9V17h16V9.9l-8 5.5z"/></svg>
    </li>
    <li>www.brackenfoldlatches.com
      <svg class="contact-icon" viewBox="0 0 24 24"><path d="M12 2a10 10 0 1 0 0 20 10 10 0 0 0 0-20zm6.9 9h-3a15 15 0 0 0-1.3-5.8A8 8 0 0 1 18.9 11zM12 4.1c.9 1.2 1.8 3.6 1.9 6.9h-3.8c.1-3.3 1-5.7 1.9-6.9zM9.4 5.2A15 15 0 0 0 8.1 11h-3a8 8 0 0 1 4.3-5.8zM5.1 13h3a15 15 0 0 0 1.3 5.8A8 8 0 0 1 5.1 13zm6.9 6.9c-.9-1.2-1.8-3.6-1.9-6.9h3.8c-.1 3.3-1 5.7-1.9 6.9zm2.6-1.1a15 15 0 0 0 1.3-5.8h3a8 8 0 0 1-4.3 5.8z"/></svg>
    </li>
  </ul>

  <p class="credentials">Fully Insured | PVX Checked</p>
  <div class="gold-strip"></div>
</section>

</body>
</html>
```